ORBIT Freight Lane Inc is a shipping company focusing on small parcel ecommerce shipments. Parcels shipments like you would receive from Marketvale or Tradowen. We have amazing shipping rates for both domestic and international shipping. We will offer a full service solution with tracking of the parcel from beginning to end customer. We will employ state of the art technology in our shipping solution and also provide an easy to use interface that integrates with Cartlofter and the other top shipping platforms.

Target Market(s)

ecommerce shipping companies, marketvale sellers, small businesses, 3PL's

Coding

Coded - Design and coding required

Number of Pages Required

3 page

Requirements
Must have
• A login page which takes you to our dashboard interface
Package tracking on UI page
Nice to have
• A technology look and feel. The UX of the site should make the viewer feel that they are using the best most technologically advanced shipping solution on the market

We will also be tying this service as a value add to our sister company www.zelnor-example.com They should not look the same as they are separate companies, but would be nice if they had a similar flare
Should not have
• Warehouse 3PL feel with people delivering boxes. We do not deliver and are not a 3PL, we are a technological platform for shipping, specializing in international parcel rates.

```html
<!DOCTYPE html>
<html lang="en">
<head>
<meta charset="UTF-8">
<title>ORBIT Freight Lane Inc – Get started</title>
<link rel="stylesheet" href="https://fonts.googleapis.com/css2?family=Outfit:wght@300;400;500;600&display=swap">
<style>
  :root {
    --hero-deep: #1747c4;
    --hero-mid: #2a7fd0;
    --hero-teal: #22b4bf;
    --accent: #35d0cc;
    --white: #ffffff;
    --ink: #111111;
    --field-border: #c9c9c9;
    --placeholder: #555555;
  }
  * { margin: 0; padding: 0; box-sizing: border-box; }
  html, body {
    width: 1200px; height: 675px; overflow: hidden;
    background: var(--white);
    font-family: "Outfit", sans-serif;
  }
  .page { position: relative; width: 1200px; height: 675px; }

  .hero {
    position: absolute; left: 0; top: 0; width: 611px; height: 675px;
    overflow: hidden; color: var(--white);
  }
  .hero-photo {
    position: absolute; inset: 0;
    background: linear-gradient(160deg, var(--hero-deep) 0%, var(--hero-mid) 50%, var(--hero-teal) 100%);
  }
  .brand {
    position: absolute; left: 184px; top: 34px;
    font-weight: 500; font-size: 26px; line-height: 1;
    color: var(--white);
  }
  .headline {
    position: absolute; left: 180px; top: 213px;
    font-weight: 500; font-size: 95px; line-height: 90px; letter-spacing: -1.5px;
  }
  .tagline {
    position: absolute; left: 185px; top: 422px;
    font-weight: 300; font-size: 19px; line-height: 23px;
  }

  .signup {
    position: absolute; left: 733px; top: 120px; width: 283px;
  }
  .signup-title {
    font-weight: 400; font-size: 37px; line-height: 1; color: var(--ink);
  }
  .signup-rule {
    width: 52px; height: 3px; background: var(--accent); margin-top: 20px;
  }
  .field {
    display: block; width: 283px; height: 41px; margin-top: 15px;
    border: 1.5px solid var(--field-border); border-radius: 21px;
    padding-left: 30px; font-family: "Outfit", sans-serif;
    font-size: 12px; color: var(--placeholder); background: var(--white);
  }
  .signup-rule + .field { margin-top: 23px; }
  .field::placeholder { color: var(--placeholder); }
  .cta {
    display: block; margin-top: 38px; width: 171px; height: 41px;
    border: none; border-radius: 21px; background: var(--accent);
    color: var(--white); font-family: "Outfit", sans-serif;
    font-weight: 600; font-size: 15px; text-align: left; padding-left: 31px;
  }
</style>
</head>
<body>
<main class="page">
  <section class="hero">
    <div class="hero-photo" role="img" aria-label="Blue-tinted photo of a person typing on a laptop at a desk"></div>
    <div class="brand">ORBIT</div>
    <h1 class="headline">Box It,<br>Move It.</h1>
    <p class="tagline">Lorem ipsum dolor sit amet, consectetur<br>adipiscing elit, sed do eiusmod.</p>
  </section>

  <form class="signup">
    <h2 class="signup-title">Get started</h2>
    <div class="signup-rule"></div>
    <input class="field" type="text" placeholder="First name">
    <input class="field" type="text" placeholder="Last name">
    <input class="field" type="email" placeholder="Email">
    <input class="field" type="password" placeholder="Password">
    <input class="field" type="password" placeholder="Repeat Password">
    <button class="cta" type="button">Contact Us now!</button>
  </form>
</main>
</body>
</html>
```